VBN Line Card

We are looking for a line card to leave with potential customers.
Logo on top

VBN is a Colorado-based business specializing in demolition, materials management, hazardous materials management, and trucking & hauling. What differentiates VBN is our breadth of experience in upcycling much of reusable debris from the demolition process for reuse on existing projects or recycling the material for later use on other projects.

We offer an end-to-end client experience that includes seamless communication, budgeting, staffing, on-site organization, and solid, quality work every time.

Trucking and Hauling Equipment:
30 yd End Dump
Steel Side Scrap Trailer
90 yr End Dump
Flatbeds
70 Ton Lowboy Trailer 2-3-2 combo

Gordon Ellery
President
720-463-9170
gellery@vbnmetalworks.com

I'd like it to be easy to read, but look modern

Target Market(s)

General Contractors

Industry/Entity Type

Construction

Colors
EB3D1F
EC4F4E
F09395
F8D3D4
FCEDEE

Requirements
Must have
• Our colors and red and gun metal gray

```html
<!DOCTYPE html>
<html lang="en">
<head>
<meta charset="utf-8">
<title>VBN Line Card</title>
<link rel="stylesheet" href="https://fonts.googleapis.com/css2?family=Lato:ital,wght@0,400;0,700;0,900;1,400;1,700&display=swap">
<style>
  :root {
    --brand-red: #8e1a1d;
    --brand-red-deep: #5a0d10;
    --ember: #c4532a;
    --ink: #1f1f22;
    --paper: #ffffff;
    --backdrop: #e9eaec;
  }
  * { margin: 0; padding: 0; box-sizing: border-box; }
  html, body {
    width: 1200px; height: 1200px; overflow: hidden;
    background: var(--backdrop);
    font-family: "Lato", Arial, sans-serif;
  }
  .line-card {
    position: absolute; left: 240px; top: 90px;
    width: 720px; height: 1019px;
    background: var(--paper);
    overflow: hidden;
  }
  .card-shapes { position: absolute; inset: 0; width: 720px; height: 1019px; }
  .wordmark {
    position: absolute; top: 62px; left: 0; width: 100%;
    text-align: center;
    font-weight: 900; font-size: 92px; letter-spacing: 14px;
    color: var(--brand-red); line-height: 1;
  }
  .intro {
    position: absolute; left: 40px; top: 172px; width: 630px;
    font-size: 16.5px; line-height: 21px; color: var(--ink);
  }
  .intro p + p { margin-top: 21px; }
  .equipment-heading {
    position: absolute; left: 40px; top: 393px;
    font-weight: 700; font-style: italic; font-size: 25px;
    color: var(--paper);
  }
  .equipment-list {
    position: absolute; left: 40px; top: 470px;
    list-style: none; font-size: 19px; line-height: 25.5px; color: var(--ink);
  }
  .equipment-list li::before { content: "• "; }
  .contact-name {
    position: absolute; left: 40px; top: 961px;
    color: var(--paper); font-size: 15px; font-weight: 700; font-style: italic;
  }
  .contact-name .title { font-size: 11px; font-weight: 400; }
  .contact-details {
    position: absolute; right: 36px; top: 959px;
    color: var(--paper); font-size: 17.5px;
  }
</style>
</head>
<body>
  <div class="line-card">
    <svg class="card-shapes" viewBox="0 0 576 815" preserveAspectRatio="none">
      <defs>
        <linearGradient id="truckPhotoTone" x1="0" y1="0" x2="1" y2="1">
          <stop offset="0" stop-color="#3a0d0e"/>
          <stop offset="0.55" stop-color="#7a2a1a"/>
          <stop offset="0.8" stop-color="#c4532a"/>
          <stop offset="1" stop-color="#2a0a0a"/>
        </linearGradient>
      </defs>
      <polygon points="0,522 208,732 0,732" fill="var(--brand-red)"/>
      <g role="img" aria-label="Photo of an orange container truck on a dark red-lit industrial road">
        <polygon points="548,302 576,302 576,732 208,732 126,649 455,302" fill="url(#truckPhotoTone)"/>
      </g>
      <polygon points="0,311 395,311 364,349 0,349" fill="var(--brand-red)"/>
      <rect x="0" y="732" width="576" height="83" fill="var(--brand-red)"/>
    </svg>

    <div class="wordmark">VBN</div>

    <div class="intro">
      <p>VBN is a Colorado-based business specializing in demolition, materials management, hazardous materials management, and trucking &amp; hauling. What differentiates VBN is our breadth of experience in upcycling much of reusable debris from the demolition process for reuse on existing projects or recycling the material for later use on other projects.</p>
      <p>We offer an end-to-end client experience that includes seamless communication, budgeting, staffing, on-site organization, and solid, quality work every time.</p>
    </div>

    <h2 class="equipment-heading">Trucking and Hauling Equipment:</h2>
    <ul class="equipment-list">
      <li>30 yd End Dump</li>
      <li>Steel Side Scrap Trailer</li>
      <li>90 yr End Dump</li>
      <li>Flatbeds</li>
      <li>70 Ton Lowboy Trailer 2-3-2 combo</li>
    </ul>

    <div class="contact-name">Gordon Ellery, <span class="title">President</span></div>
    <div class="contact-details">720-463-9170 | gellery@vbnmetalworks.com</div>
  </div>
</body>
</html>
```